A6 Advertising Post Card

I am looking for refinement on this idea for an advertising letter-box drop of an A6 postcard.
Side 1 - our brand, the address, "15% discount if you present this card before Dec 31"

We are a new retail concept in terms of the store concept.

Side 2 - i want to highlight where the products are from, what materials are used, emphasis on cool, fresh, different, affordable, the product ranges grouped by colours (storage &organisation items in 1 colour or font, illumination products in 1 colour or font, furniture in 1 colour or font, decor in 1 colour or font, curios is 1 colour or font, fasion in 1 colour or font, others in a 1 colour or font)

The Product Categories:
see attachment

Hi

I've added the product categories with products sorted under each heading. I have also added the logo in a variety of file types (jpg, tif, psd, png). The sky blue background is part of the brand image.
Thanks

Target Market(s)

Home-makers (men and women) and women of all ages. Decision makers for home furnishings. Cross demographic - this is not premium..affordable to all social strata.
The brand is about fun, colourful and functional home stuff. The fashion stuff is a small percentage of the overall offer - targeting women who should spoil themselves as they spoil their families with nice stuff for the home.

Industry/Entity Type

Advertising

```html
<!DOCTYPE html>
<html lang="en">
<head>
<meta charset="utf-8">
<title>Pasara postcard – front and back</title>
<link rel="stylesheet" href="https://fonts.googleapis.com/css2?family=PT+Sans+Narrow:wght@400;700&family=Nunito:wght@500&display=swap">
<style>
  :root{
    --canvas:#e1e1e1;
    --sky:#67c5d2;
    --navy:#1f2a55;
    --navy-soft:#2f3557;
    --plum:#3a2d5a;
    --violet:#4a2a6a;
    --white:#ffffff;
    --curl-light:#f4f5f8;
    --curl-dark:#9a9fb6;
    --sticker-a:#5a5f86;
    --sticker-b:#33385e;
    --illumination:#9b97b3;
    --storage:#f08a5a;
    --curios:#8ecfd8;
    --furniture:#4a62a8;
    --decor:#f0e21a;
    --fashion:#3e6a2a;
    --misc:#7a8a5a;
  }
  *{margin:0;padding:0;box-sizing:border-box}
  html,body{width:1200px;height:1000px;overflow:hidden}
  body{background:var(--canvas);font-family:"PT Sans Narrow",Arial,sans-serif;position:relative}
  .card{position:absolute;left:294px;width:612px;height:434px;background:var(--sky);overflow:hidden;box-shadow:0 1px 4px rgba(0,0,0,.2)}
  .card--front{top:53px}
  .card--back{top:514px}
  .card svg.shapes{position:absolute;left:0;top:0}

  /* front */
  .brand-name{position:absolute;left:130px;top:62px;font-size:118px;font-weight:700;color:var(--furniture);letter-spacing:2px;line-height:1}
  .brand-tagline{position:absolute;left:236px;top:244px;font-family:"Nunito",Arial,sans-serif;font-weight:500;font-size:29px;color:var(--violet);display:flex;align-items:center;gap:14px}
  .brand-tagline .diamond{width:14px;height:14px;background:#6a6d8a;transform:rotate(45deg);display:inline-block}
  .contact{position:absolute;right:26px;top:382px;text-align:right;color:var(--white);font-size:15px;line-height:23px}
  .offer{position:absolute;left:44px;top:262px;width:150px;transform:rotate(-20deg);color:var(--white);text-align:center;line-height:1}
  .offer__value{font-size:52px;font-weight:700}
  .offer__label{font-size:29px;font-weight:700;margin-top:-2px}
  .offer__terms{font-size:12px;line-height:13px;margin-top:4px}

  /* back */
  .headline{position:absolute;left:42px;top:28px;color:var(--white);font-size:22px;font-weight:700}
  .values{position:absolute;left:42px;top:56px;color:var(--white);font-size:14px}
  .mini-brand{position:absolute;right:26px;top:40px;font-size:30px;font-weight:700;color:var(--furniture)}
  .origins{position:absolute;left:42px;top:110px;font-size:14px;line-height:18px;font-style:italic;color:var(--navy);word-spacing:1px}
  .photo{position:absolute;top:146px;height:100px}
  .range{position:absolute;top:246px;bottom:0;padding:27px 0 0 8px;color:var(--white);font-size:10px;line-height:12.2px;list-style:none;white-space:nowrap;letter-spacing:-.2px}
  .range--short{bottom:auto}
  .range--decor{color:var(--navy)}
  .range-label{position:absolute;writing-mode:vertical-rl;transform:rotate(180deg);font-size:14px;font-weight:700;line-height:1}
</style>
</head>
<body>

<section class="card card--front">
  <svg class="shapes" width="612" height="434" viewBox="0 0 612 434">
    <path d="M0 372 C150 392 300 342 450 352 S580 362 612 348 L612 434 L0 434Z" fill="var(--navy)"/>
    <path d="M0 362 C150 382 300 332 450 342 S580 352 612 338" fill="none" stroke="var(--navy)" stroke-width="1.5"/>
    <path d="M0 367 C150 387 300 337 450 347 S580 357 612 343" fill="none" stroke="var(--white)" stroke-width="1" opacity=".6"/>
    <defs>
      <radialGradient id="stickerFill" cx="45%" cy="40%" r="70%">
        <stop offset="0" stop-color="var(--sticker-a)"/>
        <stop offset="1" stop-color="var(--sticker-b)"/>
      </radialGradient>
      <linearGradient id="curlFill" x1="0" y1="1" x2="1" y2="0">
        <stop offset="0" stop-color="var(--curl-dark)"/>
        <stop offset=".55" stop-color="var(--curl-light)"/>
        <stop offset="1" stop-color="var(--white)"/>
      </linearGradient>
    </defs>
    <circle cx="118" cy="330" r="98" fill="var(--white)"/>
    <circle cx="118" cy="330" r="90" fill="url(#stickerFill)"/>
    <path d="M122 434 C150 424 178 404 196 378 C204 366 208 356 210 348 C200 392 176 420 150 434Z" fill="url(#curlFill)" stroke="var(--white)" stroke-width="1"/>
  </svg>
  <div class="brand-name">Pasara</div>
  <div class="brand-tagline">home <span class="diamond"></span> gifts</div>
  <div class="offer">
    <div class="offer__value">15%</div>
    <div class="offer__label">DISCOUNT</div>
    <div class="offer__terms">*15% discount if you present this card before Dec 31 2013</div>
  </div>
  <div class="contact">
    <div>42 Market Lane &nbsp;| Eastwood SA 5063</div>
    <div>www.pasara.com.au</div>
  </div>
</section>

<section class="card card--back">
  <svg class="shapes" width="612" height="434" viewBox="0 0 612 434">
    <path d="M0 146 C150 134 300 150 450 140 S580 138 612 136 L612 434 L0 434Z" fill="var(--plum)"/>
    <path d="M0 140 C150 128 300 144 450 134 S580 132 612 130" fill="none" stroke="var(--navy)" stroke-width="1.5"/>
    <path d="M0 143 C150 131 300 147 450 137 S580 135 612 133" fill="none" stroke="var(--white)" stroke-width="1" opacity=".6"/>
    <path d="M0 236 C150 250 300 226 450 236 S580 240 612 230 L612 434 L0 434Z" fill="var(--navy-soft)"/>
  </svg>
  <div class="headline">A new store concept</div>
  <div class="values">Fresh • Cool • Exotic • Modern</div>
  <div class="mini-brand">Pasara</div>
  <div class="origins">From India • Philippines • Thailand • Indonesia • Malaysia • Nepal • Cambodia</div>

  <div class="photo" style="left:0;width:109px;background:linear-gradient(135deg,#6b5a3a,#8a9a5a,#5a3a2a)" role="img" aria-label="Photo of assorted curios and ornaments"></div>
  <div class="photo" style="left:116px;width:120px;background:linear-gradient(180deg,#f2f2f2,#b06a6a 45%,#f2f2f2)" role="img" aria-label="Photo of a patterned storage box"></div>
  <div class="photo" style="left:243px;width:118px;background:linear-gradient(180deg,#2a2a2a,#8a6a4a 60%,#2a2a2a)" role="img" aria-label="Photo of a woven planter with plant"></div>
  <div class="photo" style="left:366px;width:118px;background:linear-gradient(120deg,#e6e2dc,#7a9ac0,#d86a6a,#e6e2dc)" role="img" aria-label="Photo of striped cushions"></div>
  <div class="photo" style="left:490px;width:122px;background:linear-gradient(135deg,#c08a5a,#e0b07a,#7a7a7a)" role="img" aria-label="Photo of woven baskets and figurines"></div>

  <span class="range-label" style="left:30px;top:272px;color:var(--illumination)">Illumination</span>
  <ul class="range" style="left:43px;width:77px;background:var(--illumination)">
    <li>Glass Votives</li><li>Lamps</li><li>Moroccan Lanterns</li><li>Chandeliers</li><li>Candle Holders</li><li>Candles</li><li>Tee-light Holders</li><li>Pendant Lights</li><li>Lantern Stands</li>
  </ul>

  <span class="range-label" style="left:124px;top:272px;color:var(--storage)">Storage &amp; Organisation</span>
  <ul class="range" style="left:136px;width:79px;background:var(--storage)">
    <li>Baskets</li><li>Trays</li><li>Drawers</li><li>Boxes</li><li>Tiffin Carriers</li><li>Plates</li><li>Bowls</li><li>Napkin Rings</li><li>Bamboo Towel Stands</li><li>Mugs</li><li>Cups</li><li>Jugs</li>
  </ul>

  <span class="range-label" style="left:216px;top:272px;color:var(--curios)">Curios</span>
  <ul class="range" style="left:228px;width:79px;background:var(--curios)">
    <li>Figurines</li><li>Brass Statues</li><li>Telescopes</li><li>Compasses</li><li>Hour Glasses</li><li>Sextants</li><li>Magnifying Lens</li><li>Prayer Wheels</li><li>Singing Bowls</li><li>Incense Holder</li><li>Musical Instruments</li>
  </ul>

  <span class="range-label" style="left:309px;top:272px;color:var(--furniture)">Furniture</span>
  <ul class="range" style="left:321px;width:79px;background:var(--furniture)">
    <li>Cupboards</li><li>Tables</li><li>Stools</li><li>Chairs</li><li>Bookcases</li><li>Consoles</li><li>Carts</li><li>Trolleys</li><li>Ceramic Knobs</li><li>Ladders</li><li>Umbrellas</li><li>Planters</li>
  </ul>

  <span class="range-label" style="left:402px;top:272px;color:var(--decor)">Decor</span>
  <ul class="range range--decor" style="left:414px;width:79px;background:var(--decor)">
    <li>Cushions</li><li>Photo-frames</li><li>Decorative Ornaments</li><li>Vases</li><li>Bowls</li><li>Clocks</li><li>Mirrors</li><li>Bird Cages</li><li>Sedge Mats</li><li>Glass Decanters</li><li>Pattachitra Bottles</li><li>Bird Cage Stands</li>
  </ul>

  <span class="range-label" style="left:496px;top:272px;color:var(--fashion)">Fashion</span>
  <ul class="range range--short" style="left:508px;width:78px;height:109px;background:var(--fashion);padding-top:24px">
    <li>Shawls</li><li>Scarves</li><li>Bags</li><li>Bangles</li><li>Flip-Flops</li>
  </ul>

  <span class="range-label" style="left:496px;top:350px;color:var(--misc)">Miscellaneous</span>
  <ul class="range" style="top:348px;left:508px;width:78px;background:var(--misc);padding-top:8px">
    <li>Gift Bags</li><li>Wrapping Paper</li><li>Wine Bottle Holder</li><li>Xmas Decorations</li>
  </ul>
</section>

</body>
</html>
```